Web Design Front Page Only for Organic Skincare

We have been in business for nearly 20 years. We are run by all females and sell anything from aromatherapy, skincare and pharmacy types products to health food shops and pharmacy. We are looking for an attractive and colourful but simple front web page design for our wholesale customers to look at. We want our customers to start using our website to find information rather than ringing us. So we want it to be attractive to our buyers who are young and funky.
Updates

To give you an idea of the products we sell to pharmacy and health food shops also beauty shops and hair salons.  We mainly deal with organic body and skincare, aromatherapy oils and body products, but also do some simple pharmacy products such as bandages and pill boxes, finger splits, walking frames and wheelchairs.  We are only looking for the front page of the website.  The back-end will be done in-house.  We currently do not have a logo designed so I am thinking that once we have done the website design we can build a logo from it.  I like bright colours and want something that is inviting to further discover that we do many different types of products.

Target Market(s)

young girls who are our retail buyers

Industry/Entity Type

Pharmacy

Requirements
Must have
• A section which says

Customer Log in
Should not have
• don't worry about too much writing or tabs. We will insert these later. Just come up with design image.

```html
<!DOCTYPE html>
<html lang="en">
<head>
<meta charset="utf-8">
<title>Leafwell Healthcare</title>
<link rel="stylesheet" href="https://fonts.googleapis.com/css2?family=PT+Serif:wght@400;700&family=PT+Sans:wght@400;700&family=Oswald:wght@400;600&display=swap">
<style>
:root{
  --green-dark:#2f7a0c;
  --green:#5a9a1c;
  --green-light:#8cbc2c;
  --lime:#a3c43a;
  --purple:#9b14c9;
  --purple-dark:#7a0fa0;
  --orange:#f08c10;
  --orange-dark:#d86a00;
  --text:#3a3a3a;
  --muted:#8a8a8a;
  --line:#d8d8d8;
  --page:#ececec;
  --footer:#d6ebb2;
  --white:#fff;
}
*{box-sizing:border-box;margin:0;padding:0}
html,body{width:960px;height:1200px;overflow:hidden}
body{position:relative;background:var(--page);font-family:"PT Sans",sans-serif;color:var(--text);font-size:9.5px}
.abs{position:absolute}
.topbar{left:0;top:0;width:960px;height:7px;background:var(--green-dark)}
.brand{left:100px;top:26px;font-family:"PT Serif",serif;font-size:28px;color:var(--lime);letter-spacing:.5px}
.brand small{font-size:17px;letter-spacing:1.5px;margin-left:6px}
.cart{left:567px;top:14px;font-size:9.5px;color:#555}
.cart b{font-weight:400;color:var(--orange);margin-left:6px}
.cart a{display:block;margin-left:48px;margin-top:2px;color:#555;text-decoration:underline}
.checkout{left:566px;top:44px;width:132px;height:20px;border-radius:10px;background:linear-gradient(#3f9b10,#1f6a04);color:#fff;text-align:center;line-height:20px;font-size:10px;border:1px solid #1a5a03}
.vsep{top:14px;width:1px;height:50px;background:var(--line)}
.account{top:18px;font-size:10.5px;color:#555;display:flex;align-items:center;gap:5px}
.search{left:729px;top:46px;width:135px;height:19px;border:1px solid #bbb;background:#fff}
.search span{position:absolute;right:-1px;top:-1px;width:26px;height:19px;background:var(--green-light)}
.nav{left:126px;top:77px;width:700px;display:flex;font-family:"PT Serif",serif;font-size:12px;color:#333}
.nav span{padding:0 22px;border-right:1px solid #bbb;line-height:18px}
.nav span:last-child{border:none}
.hrline{left:95px;width:768px;height:1px;background:var(--line)}
.hero{left:95px;top:110px;width:768px;height:310px;background:linear-gradient(100deg,#2f7a10 0%,#7ab838 40%,#b8d870 60%,#e8d0b8 80%,#d9b89a 100%)}
.hero-box{left:168px;top:178px;width:401px;height:170px;background:rgba(40,110,20,.45);border:1px solid rgba(255,255,255,.3);border-radius:3px}
.hero-title{left:208px;top:201px;font-family:"PT Serif",serif;font-weight:700;font-size:19px;color:#fff}
.hero-copy{left:206px;top:229px;width:305px;font-family:"PT Serif",serif;font-size:13.5px;line-height:17px;color:#fff}
.btn-orange{background:linear-gradient(#ffb030,var(--orange-dark));color:#fff;font-family:"PT Serif",serif;font-weight:700;text-align:center;border-radius:12px;border:1px solid #c66000}
.hero-btn{left:206px;top:300px;width:152px;height:24px;line-height:22px;font-size:9px;letter-spacing:.5px}
.card{background:#fff;border:1px solid #ddd;border-radius:3px}
.cats{left:95px;top:430px;width:208px;height:333px}
.cats-head{left:99px;top:434px;width:200px;height:30px;background:linear-gradient(var(--green-light),var(--green));color:#fff;font-family:"PT Serif",serif;font-size:13.5px;line-height:30px;padding-left:8px}
.cats-head b{font-weight:700}
.cats-list{left:104px;top:492px;width:186px;list-style:none;font-size:10px}
.cats-list li{height:22.4px;line-height:22px;border-bottom:1px dotted #ccc;padding-left:5px;position:relative}
.cats-list li.on{background:#e6e6e6}
.cats-list li.gap{margin-top:22px}
.cats-list svg{position:absolute;right:6px;top:6px}
.news{left:95px;top:775px;width:208px;height:170px}
.news-kicker{left:108px;top:788px;font-size:9px;color:#444}
.news-title{left:107px;top:798px;font-family:"PT Serif",serif;font-size:17px;color:var(--orange-dark);letter-spacing:.5px}
.news-copy{left:108px;top:822px;width:190px;font-size:9px;line-height:11.5px;color:#555}
.news-form{left:104px;top:865px;width:189px;height:69px;background:#ebebeb;border:1px solid #ddd;border-radius:3px}
.news-input{left:114px;top:872px;width:169px;height:24px;background:#fff;border:1px solid #ddd;font-size:8.5px;font-style:italic;color:#999;line-height:22px;padding-left:12px}
.subscribe{left:135px;top:905px;width:127px;height:20px;line-height:18px;font-size:11.5px}
.welcome{left:320px;top:436px;font-family:"PT Serif",serif;font-weight:400;font-size:15px;color:#222}
.welcome span{color:var(--lime);font-size:20px}
.intro{left:321px;top:478px;width:530px;font-size:9.2px;line-height:11.5px;color:#444}
.intro p{margin-bottom:8px}
.tabs{left:344px;top:615px;display:flex;gap:34px;font-size:12.5px;letter-spacing:.5px;color:#aaa}
.tabs .on{color:var(--purple)}
.products{left:320px;top:637px;width:544px;height:175px}
.thumb{top:656px;width:134px;height:108px;border:1px solid #ddd;background:#fff}
.thumb.on{border-color:var(--purple)}
.thumb div{margin:14px;height:78px;border-radius:40px}
.pname{top:767px;width:160px;text-align:center;font-size:9.2px;line-height:12px;color:#444}
.price{top:792px;width:66px;height:12px;border-radius:6px;background:var(--purple);color:#fff;font-size:9.5px;line-height:12px;text-align:center}
.arrow{top:704px;width:20px;height:20px;border-radius:50%;background:#bbb;border:2px solid #eee}
.promo{top:824px;height:121px;border-radius:3px;overflow:hidden}
.promo-chairs{left:320px;width:285px;background:linear-gradient(90deg,#6a8aa8,#a8bccc)}
.promo-pharm{left:613px;width:252px;background:linear-gradient(100deg,#d9d9d9 40%,#e8a020 75%,#d85a00)}
.promo-title{font-family:"PT Serif",serif;color:#fff}
.footband{left:0;top:968px;width:960px;height:17px;background:var(--green-dark)}
.footer{left:0;top:985px;width:960px;height:215px;background:var(--footer)}
.fhead{font-size:14px;color:var(--green-dark)}
.flist{font-size:8.5px;line-height:14.4px;color:#444;list-style:none}
.ficon{border-radius:50%}
.pay{width:30px;height:17px;border-radius:2px}
.social{font-size:9.5px;color:#666;line-height:24px;list-style:none}
.social li{display:flex;align-items:center;gap:8px}
.social i{display:inline-block;width:20px;height:20px;border-radius:50%;border:2px solid #fff}
.flinks{left:0;width:960px;text-align:center;font-size:9px;color:#666}
.flinks span+span{border-left:1px solid #999;padding-left:5px;margin-left:4px}
.flinks.alt{color:var(--orange-dark)}
</style>
</head>
<body>
<div class="abs topbar"></div>

<header>
  <div class="abs brand">leafwell<small>HEALTHCARE</small></div>
  <div class="abs cart">Your Cart:<b>2 items</b><a>View cart</a></div>
  <svg class="abs" style="left:668px;top:12px" width="26" height="26" viewBox="0 0 26 26" aria-hidden="true"><path d="M2 4h4l3 12h12l3-9H8" fill="none" stroke="#888" stroke-width="1.6"/><circle cx="10" cy="21" r="2" fill="#c33"/><circle cx="19" cy="21" r="2" fill="#c33"/></svg>
  <div class="abs checkout">Checkout</div>
  <div class="abs vsep" style="left:548px"></div>
  <div class="abs vsep" style="left:712px"></div>
  <div class="abs account" style="left:728px">
    <svg width="12" height="12" viewBox="0 0 12 12" aria-hidden="true"><circle cx="8" cy="4" r="3" fill="none" stroke="#888" stroke-width="1.5"/><path d="M6 6L1 11" stroke="#888" stroke-width="1.5"/></svg>Login</div>
  <div class="abs account" style="left:798px">
    <svg width="12" height="12" viewBox="0 0 12 12" aria-hidden="true"><path d="M2 10L10 2" stroke="#888" stroke-width="2"/></svg>Register</div>
  <div class="abs search"><span></span>
    <svg class="abs" style="right:6px;top:3px" width="12" height="12" viewBox="0 0 12 12" aria-hidden="true"><circle cx="5" cy="5" r="3.5" fill="none" stroke="#fff" stroke-width="1.6"/><path d="M7.5 7.5L11 11" stroke="#fff" stroke-width="2"/></svg></div>
  <div class="abs hrline" style="top:70px"></div>
  <nav class="abs nav"><span>Home</span><span>About Us</span><span>Health Food</span><span>Pharmacy</span><span>Beauty</span><span>Supermarket</span><span>Contact Us</span></nav>
  <div class="abs hrline" style="top:104px"></div>
</header>

<section>
  <div class="abs hero" role="img" aria-label="Green aloe leaves with a water droplet and a smiling woman, fresh skincare mood"></div>
  <div class="abs hero-box"></div>
  <h2 class="abs hero-title">DONEC EU QUAM LIGULA</h2>
  <p class="abs hero-copy">Nullam turpis ante, faucibus eu ornare at, aliquet eget nisl. Nam elit neque, hendrerit nec sodales at, aliquam et nisl</p>
  <div class="abs btn-orange hero-btn">FIND OUT MORE &#9656;</div>
</section>

<aside>
  <div class="abs card cats"></div>
  <div class="abs cats-head">Product <b>Categories</b></div>
  <svg class="abs" style="left:272px;top:463px" width="16" height="9" aria-hidden="true"><path d="M0 0h16L8 9z" fill="#5a9a1c"/></svg>
  <ul class="abs cats-list">
    <li class="on">Face<svg width="18" height="11"><path d="M0 11L9 1l9 10z" fill="#6a3a8a"/></svg></li>
    <li>Body<svg width="18" height="11"><path d="M0 11L9 1l9 10z" fill="#6a3a8a"/></svg></li>
    <li>Hair<svg width="18" height="11"><path d="M0 11L9 1l9 10z" fill="#6a3a8a"/></svg></li>
    <li>Hands Care<svg width="18" height="11"><path d="M0 11L9 1l9 10z" fill="#6a3a8a"/></svg></li>
    <li>Feet Care<svg width="18" height="11"><path d="M0 11L9 1l9 10z" fill="#6a3a8a"/></svg></li>
    <li>Eye Products<svg width="18" height="11"><path d="M0 11L9 1l9 10z" fill="#6a3a8a"/></svg></li>
    <li>Aromatherapy Oils<svg width="18" height="11"><path d="M0 11L9 1l9 10z" fill="#6a3a8a"/></svg></li>
    <li class="gap">Pharmacy Products<svg width="18" height="11"><path d="M0 11L9 1l9 10z" fill="#6a3a8a"/></svg></li>
    <li class="gap" style="margin-top:25px">Other Leafwell Products<svg width="18" height="11"><path d="M0 11L9 1l9 10z" fill="#6a3a8a"/></svg></li>
  </ul>

  <div class="abs card news"></div>
  <div class="abs news-kicker">SIGNUP FOR OUR</div>
  <div class="abs news-title">FREE NEWSLETTER</div>
  <p class="abs news-copy">Subscribe to our free newsletter to receive up-to-date information on new products and promos!</p>
  <div class="abs news-form"></div>
  <div class="abs news-input">Enter email address here</div>
  <div class="abs btn-orange subscribe">SUBSCRIBE</div>
</aside>

<main>
  <h1 class="abs welcome">Welcome to <span>LEAFWELL HEALTHCARE</span></h1>
  <div class="abs intro">
    <p>Nam viverra velit sem, vel iaculis nisl. Pellentesque vel elit lorem. Sed molestie mauris sed purus egestas eget ultricies velit aliquam. Vestibulum ante ipsum primis in faucibus orci luctus et ultrices posuere cubilia Curae; Maecenas sit amet risus nec sem scelerisque consectetur eget sit amet purus. Curabitur dignissim, enim in vestibulum posuere, est nibh rutrum nisl, sit amet interdum lorem mauris at ligula. Maecenas eu nisl et quam laoreet luctus sit amet posuere ligula. Etiam condimentum porttitor tempor. Praesent sodales sem quis mauris consectetur ac volutpat mauris pharetra. Sed non sem vel orci tincidunt semper vel vel lectus. Donec tincidunt lectus lectus, bibendum feugiat lectus.</p>
    <p>Aliquam ante leo, suscipit ultrices dapibus at, fermentum non est. Proin tempor felis sit amet odio blandit tristique. Suspendisse eu mauris imperdiet ipsum sagittis ultricies. Nam viverra velit sem, vel iaculis nisl. Pellentesque vel elit lore. Sed molestie mauris sed purus egestas eget ultricies velit aliquam.</p>
  </div>

  <div class="abs tabs"><span class="on">TOP PRODUCTS</span><span>LATEST PRODUCTS</span><span>THE SPECIALS</span></div>
  <div class="abs card products"></div>
  <svg class="abs" style="left:378px;top:637px" width="16" height="9" aria-hidden="true"><path d="M0 0h16L8 9z" fill="#ddd"/><path d="M1 0h14L8 8z" fill="#fff"/></svg>
  <div class="abs arrow" style="left:310px"><svg width="16" height="16" viewBox="0 0 16 16"><path d="M10 4L5 8l5 4z" fill="#fff"/></svg></div>
  <div class="abs arrow" style="left:852px"><svg width="16" height="16" viewBox="0 0 16 16"><path d="M6 4l5 4-5 4z" fill="#fff"/></svg></div>

  <div class="abs thumb" style="left:364px"><div role="img" aria-label="Pink roses and bath pearls" style="background:radial-gradient(#f07090,#fbe0e6)"></div></div>
  <div class="abs thumb" style="left:515px"><div role="img" aria-label="Lavender oil bottle with lilac soap" style="background:radial-gradient(#9a7ac8,#ece6f4)"></div></div>
  <div class="abs thumb on" style="left:665px"><div role="img" aria-label="Honey jar with sponge" style="background:radial-gradient(#f0b840,#fbf0d8)"></div></div>
  <p class="abs pname" style="left:351px">Lorem ipsum dolorsit<br>amet conscec</p>
  <p class="abs pname" style="left:502px">Lorem ipsum dolorsit<br>amet conscec</p>
  <p class="abs pname" style="left:657px">Lorem ipsum dolorsit<br>amet conscec</p>
  <div class="abs price" style="left:400px">$20.00</div>
  <div class="abs price" style="left:550px">$20.00</div>
  <div class="abs price" style="left:704px">$20.00</div>

  <div class="abs promo promo-chairs" role="img" aria-label="Wheelchair and walking frame"></div>
  <div class="abs promo-title" style="left:420px;top:830px;font-size:22px;letter-spacing:1px">WHEELCHAIRS</div>
  <div class="abs promo-title" style="left:427px;top:856px;font-size:13px;letter-spacing:1px">And WALKING FRAMES</div>
  <div class="abs" style="left:428px;top:878px;width:165px;text-align:center;color:#fff;font-size:10.5px;line-height:13px">Lorem ipsum dolor sit amet ore ipsum dolor sit amet</div>
  <div class="abs" style="left:440px;top:910px;width:144px;height:22px;background:rgba(255,255,255,.2);text-align:center;font-family:Oswald,sans-serif;color:#fff;font-size:13px;line-height:22px">Lorem ipsum dolor</div>

  <div class="abs promo promo-pharm" role="img" aria-label="Medical supplies on a light background"></div>
  <div class="abs" style="left:627px;top:828px;font-family:Oswald,sans-serif;font-weight:600;color:#fff;font-size:22px">Pharmacy Products</div>
  <div class="abs" style="left:631px;top:859px;font-family:Oswald,sans-serif;color:var(--orange-dark);font-size:13px">Lorem ipsum dolor sit amet</div>
  <ul class="abs" style="left:636px;top:890px;font-family:'PT Serif',serif;font-style:italic;font-weight:700;color:#c40;font-size:9.5px;line-height:13px">
    <li>Lorem ipsum dolor sit</li><li>Ipsum dolor sit amet</li><li>Ipsum dolor sit amet</li></ul>
  <div class="abs" style="left:796px;top:874px;color:#fff;font-size:9.5px;line-height:12px">Click here<br>for details</div>
  <div class="abs" style="left:814px;top:904px;width:26px;height:26px;border-radius:50%;background:rgba(255,255,255,.5)"><svg width="26" height="26" viewBox="0 0 26 26"><path d="M10 7l9 6-9 6z" fill="#fff"/></svg></div>
</main>

<footer>
  <div class="abs footband"></div>
  <div class="abs footer"></div>

  <div class="abs fhead" style="left:95px;top:1008px">help</div>
  <div class="abs ficon" style="left:97px;top:1027px;width:22px;height:22px;background:#1aa0e0"></div>
  <ul class="abs flist" style="left:134px;top:1011px"><li>Help</li><li>FAQs</li><li>Contact Us</li><li>Returns</li><li>Shipping info</li></ul>

  <div class="abs fhead" style="left:254px;top:1008px">about</div>
  <div class="abs ficon" style="left:260px;top:1029px;width:22px;height:22px;background:#4aa0e0"></div>
  <ul class="abs flist" style="left:301px;top:1011px"><li>About leafwell healthcare</li><li>Affiliates</li><li>Privacy Policy</li><li>Terma adn Conditions</li><li>Disclaimer</li></ul>

  <div class="abs fhead" style="left:486px;top:1008px">payment</div>
  <div class="abs" style="left:502px;top:1035px;width:24px;height:13px;background:#3aa0e0;border-radius:2px"></div>
  <div class="abs pay" style="left:555px;top:1012px;background:#e8eef8"></div>
  <div class="abs pay" style="left:590px;top:1012px;background:#fff"></div>
  <div class="abs pay" style="left:555px;top:1035px;background:#1a4aa0"></div>
  <div class="abs pay" style="left:590px;top:1035px;background:#1a4aa0"></div>
  <div class="abs pay" style="left:555px;top:1055px;background:#2a6ab0"></div>
  <div class="abs pay" style="left:590px;top:1055px;background:#c03020"></div>
  <div class="abs pay" style="left:555px;top:1076px;background:#5a8ac8"></div>
  <div class="abs pay" style="left:590px;top:1076px;background:#1a3a90"></div>

  <div class="abs fhead" style="left:712px;top:1008px">connect</div>
  <div class="abs" style="left:727px;top:1030px;width:28px;height:20px;background:#2a90d8;border-radius:2px"></div>
  <ul class="abs social" style="left:778px;top:1008px">
    <li><i style="background:#3aa8e8"></i>Chirper</li>
    <li><i style="background:#2a5aa8"></i>Facenote</li>
    <li><i style="background:#2a6aa8"></i>Linkpro</li>
    <li><i style="background:#f08020"></i>Rss Feed</li>
  </ul>

  <p class="abs flinks" style="top:1130px"><span>Face</span><span>Body</span><span>Hair</span><span>Hands Care</span><span>Feet Care</span><span>Eye Products</span><span>Aromatherapy Oils</span><span>Healthcare Tips</span><span>Healthcare Articles</span></p>
  <p class="abs flinks alt" style="top:1148px"><span>New Products</span><span>Wheelchairs</span><span>Walking Frames</span><span>Pharmacy Prodcuts</span></p>
  <p class="abs flinks" style="top:1167px">Copyright &copy; 2012 LEAFWELL HEALTHCARE. All rights reserved.</p>
</footer>
</body>
</html>
```